Family Ranch with a hobby vineyard needs 2 wine labels for our first harvest

Design 2 wine labels (front and back) with the Brindor Ranch logo.
Label 1:
Sauvignon Blanc
Alc. 12.5% by Vol.
Palos Verdes Peninsula - add as the region
Year 2022
Label 2:
Cabernet Sauvignon
Alc. 13.5% by Vol.
Year 2022
For the back label design:
GOVERNMENT WARNING: (1) According to the Surgeon General, women
should not drink alcoholic beverages during pregnancy because of the risk of
birth defects. (2) Consumption of alcoholic beverages impairs your ability to
drive a car or operate machinery, and may cause health problems.
Contains Sulfates.
750ML
I just received the bottles and have attached a picture.
Look and feel
Each slider illustrates characteristics of the customer's brand and the style your logo design should communicate.

```html
<!DOCTYPE html>
<html lang="en">
<head>
<meta charset="UTF-8">
<title>Brindor Ranch Cabernet Sauvignon 2022 Label</title>
<link rel="stylesheet" href="https://fonts.googleapis.com/css2?family=Alegreya:wght@400&family=Josefin+Sans:wght@400;600&display=swap">
<style>
  :root {
    --label-tan: #c4b59c;
    --band-brown: #5a4a40;
    --mark-ink: #2b2522;
    --text-brown: #5a4a40;
  }
  html, body {
    margin: 0;
    padding: 0;
    overflow: hidden;
    background: var(--label-tan);
  }
  .wine-label {
    position: relative;
    width: 1200px;
    height: 1050px;
    background: var(--label-tan);
    overflow: hidden;
  }
  .label-band {
    position: absolute;
    left: 68px;
    width: 1065px;
    height: 26px;
    background: var(--band-brown);
  }
  .label-band--top { top: 37px; }
  .label-band--bottom { top: 986px; }

  .brand-mark {
    position: absolute;
    left: 0;
    right: 0;
    top: 105px;
    display: flex;
    flex-direction: column;
    align-items: center;
  }
  .brand-mark__dot {
    display: block;
  }
  .brand-mark__name {
    margin-top: 42px;
    font-family: "Josefin Sans", sans-serif;
    font-weight: 600;
    font-size: 58px;
    letter-spacing: 4px;
    color: var(--mark-ink);
    text-transform: uppercase;
    line-height: 1;
  }

  .wine-varietal,
  .wine-vintage,
  .wine-region,
  .wine-abv {
    position: absolute;
    left: 0;
    right: 0;
    margin: 0;
    text-align: center;
    color: var(--text-brown);
    line-height: 1;
  }
  .wine-varietal {
    top: 560px;
    font-family: "Alegreya", serif;
    font-weight: 400;
    font-size: 70px;
    letter-spacing: 3px;
  }
  .wine-vintage {
    top: 680px;
    font-family: "Alegreya", serif;
    font-size: 58px;
    letter-spacing: 6px;
  }
  .wine-region {
    top: 826px;
    font-family: "Josefin Sans", sans-serif;
    font-weight: 400;
    font-size: 36px;
    letter-spacing: 5px;
    text-transform: uppercase;
  }
  .wine-abv {
    top: 898px;
    font-family: "Alegreya", serif;
    font-size: 38px;
    letter-spacing: 4px;
  }
</style>
</head>
<body>
  <main class="wine-label">
    <div class="label-band label-band--top"></div>

    <div class="brand-mark">
      <svg class="brand-mark__dot" width="200" height="200" viewBox="0 0 200 200" aria-hidden="true">
        <circle cx="100" cy="100" r="100" fill="var(--mark-ink)"/>
      </svg>
      <div class="brand-mark__name">Brindor Ranch</div>
    </div>

    <h1 class="wine-varietal">Cabernet Sauvignon</h1>
    <p class="wine-vintage">2022</p>
    <p class="wine-region">Palos Verdes Peninsula</p>
    <p class="wine-abv">13.5% VOL.</p>

    <div class="label-band label-band--bottom"></div>
  </main>
</body>
</html>
```